Business Card Design for Oncology Consulting Company

We need a business card design using a logo that has already been created.

Company name is: ORBVA - Guild for Lumora Mapping, Welfare and Outreach

We would also like to include the following pieces of information on the business card:
Name
Title
US Address (street, city, state, zip, country)
Email address
Website address

Target Market(s)

The target customers are physicians (oncologists, pathologists) in Greece, Iran, US, etc who would refer patients to our company for a second medical opinion/genetic counseling for cancer.

Industry/Entity Type

Business

Colors

Designer to choose colors to be used in the design.

Requirements
Must have
• Must contain logo in attached file and elements described above.

```html
<!DOCTYPE html>
<html lang="en">
<head>
<meta charset="utf-8">
<title>ORBVA Business Card</title>
<link rel="stylesheet" href="https://fonts.googleapis.com/css2?family=Ubuntu:wght@400;500;700&display=swap">
<style>
  :root {
    --brand-blue: #1f5ea8;
    --ink: #2b2b2b;
    --muted-grey: #a9a9a9;
    --rule-grey: #c8c8c8;
    --card-white: #ffffff;
    --backdrop: #e6e6e6;
    --mark-tint-blue: #dbe6f3;
    --mark-tint-grey: #ececec;
  }
  * { margin: 0; padding: 0; box-sizing: border-box; }
  html, body {
    width: 1200px; height: 960px; overflow: hidden;
    background: var(--backdrop);
    font-family: "Ubuntu", sans-serif;
  }
  .sheet {
    width: 1200px; height: 960px;
    display: flex; flex-direction: column;
    align-items: center; justify-content: center; gap: 40px;
  }
  .card {
    position: relative;
    width: 760px; height: 434px;
    background: var(--card-white);
    box-shadow: 0 6px 18px rgba(0,0,0,0.12);
  }

  /* Front */
  .brand-name {
    position: absolute; left: 52px; top: 48px;
    font-size: 88px; font-weight: 700; line-height: 1;
    color: var(--brand-blue); letter-spacing: 1px;
  }
  .mark-placeholder {
    position: absolute;
    background: linear-gradient(90deg, var(--mark-tint-grey), var(--mark-tint-blue));
  }
  .mark-placeholder.small { left: 410px; top: 44px; width: 300px; height: 50px; }
  .brand-tagline {
    position: absolute; left: 410px; top: 100px; width: 300px;
    border-top: 3px solid var(--rule-grey);
    padding-top: 4px;
    font-size: 10.5px; font-weight: 500; text-transform: uppercase;
    color: var(--muted-grey); letter-spacing: 0.2px;
    white-space: nowrap;
  }
  .dotted-rule {
    position: absolute; left: 52px; right: 52px;
    border-top: 2px dotted var(--rule-grey);
  }
  .dotted-rule.upper { top: 160px; }
  .dotted-rule.lower { top: 262px; }
  .person {
    position: absolute; left: 52px; top: 200px;
    display: flex; align-items: baseline; gap: 16px;
  }
  .person-name { font-size: 34px; color: var(--ink); }
  .person-title { font-size: 17px; color: var(--ink); text-transform: uppercase; letter-spacing: 0.5px; }
  .contact-email { position: absolute; left: 400px; top: 210px; font-size: 17px; color: var(--ink); }
  .contact-list {
    position: absolute; left: 52px; top: 284px;
    list-style: none; font-size: 18px; color: var(--ink); line-height: 40px;
  }
  .contact-label { color: var(--brand-blue); text-transform: uppercase; margin-right: 6px; }

  /* Back */
  .mark-placeholder.large { left: 70px; top: 48px; width: 620px; height: 190px; }
  .back-rule {
    position: absolute; left: 70px; right: 70px; top: 262px;
    border-top: 5px solid var(--rule-grey);
  }
  .back-tagline {
    position: absolute; left: 70px; top: 276px;
    font-size: 20px; font-weight: 500; text-transform: uppercase;
    color: var(--muted-grey); letter-spacing: 0.3px;
    white-space: nowrap;
  }
  .back-web {
    position: absolute; right: 70px; top: 340px;
    font-size: 26px; color: var(--brand-blue); letter-spacing: 0.5px;
  }
</style>
</head>
<body>
<main class="sheet">
  <section class="card card-front" aria-label="Card front">
    <div class="brand-name">ORBVA</div>
    <div class="mark-placeholder small" role="img" aria-label="Brand symbol area: rising wave of blue and grey dots"></div>
    <div class="brand-tagline">Guild for Lumora Mapping, Welfare and Outreach</div>
    <div class="dotted-rule upper"></div>
    <div class="person">
      <span class="person-name">Elias Marrow</span>
      <span class="person-title">Manager</span>
    </div>
    <div class="contact-email"><span class="contact-label">Email</span>elias.marrow@orbva.com</div>
    <div class="dotted-rule lower"></div>
    <ul class="contact-list">
      <li><span class="contact-label">Phone</span>(503) 555 0147</li>
      <li><span class="contact-label">Address</span>418 Alder St. Suite 6, Portland, OR 97205, US</li>
      <li><span class="contact-label">Web</span>www.orbva.com</li>
    </ul>
  </section>

  <section class="card card-back" aria-label="Card back">
    <div class="mark-placeholder large" role="img" aria-label="Large brand symbol decoration: rising wave of blue and grey dots"></div>
    <div class="back-rule"></div>
    <div class="back-tagline">Guild for Lumora Mapping, Welfare and Outreach</div>
    <div class="back-web">www.orbva.com</div>
  </section>
</main>
</body>
</html>
```